Brightvale Crew Word Press Website

We need a graphical, fun website that conveys our messaging of providing the Best-In-Class Signature Marketing System for Mortgage Loan Officers and Realtors. Our system uses AI and Predictive Analysis to uncover the 'Gold' hidden in contact databases. The 'Gold' is defined as people who are in the market or likely to be in the market soon. We place that 'Gold' in the form of Contact Name, Address, Phone and Email on a Daily To Do List detailing what type of contact should be made.

Target Market(s)

Mortgage Loan Officers and Realtors

Industry/Entity Type

Mortgage & Real Estate

Coding

Coded - Design and coding required

Number of Pages Required

5+ page

Requirements
Must have
• I like the look of this site- https://www.homeloanpromostudio.example/
Nice to have
• Please create a flow that is similar to https://www.homeloanpromostudio.example/, but better, more dynamic. Site must be responsive and mobile friendly. Site will have embedded videos. Site need to convey a message of hope, imagination, innovation, results oriented, better than the rest, victory!
Should not have
• Nothing cheesy or low class.

```html
<!DOCTYPE html>
<html lang="en">
<head>
<meta charset="utf-8">
<title>Brightvale Crew</title>
<link rel="stylesheet" href="https://fonts.googleapis.com/css2?family=Raleway:wght@400;500;600;700;800&display=swap">
<style>
:root{
  --blue:#1a9fdf;
  --blue-dark:#1287c4;
  --gold:#e2b43c;
  --gold-light:#f3d56a;
  --ink:#1b1b1b;
  --text:#444;
  --muted:#8a8a8a;
  --pale:#eaf5fc;
  --footer:#111214;
  --white:#fff;
}
*{box-sizing:border-box;margin:0;padding:0}
html,body{width:1200px;height:4246px;overflow:hidden}
body{font-family:"Raleway",sans-serif;color:var(--text);background:var(--white);position:relative}
.abs{position:absolute}
a{color:inherit;text-decoration:none}

/* header */
.site-header{position:absolute;left:0;top:0;width:1200px;height:200px;background:var(--white)}
.brand{position:absolute;display:flex;align-items:center;gap:10px;font-weight:800;color:var(--blue);letter-spacing:.5px}
.brand .dot{width:22px;height:22px;border-radius:50%;background:var(--gold);flex:none}
.header-brand{left:110px;top:70px;font-size:26px;width:220px;line-height:1.1}
.contact-item{position:absolute;top:28px;display:flex;align-items:center;gap:14px}
.contact-item .ring{width:62px;height:62px;border-radius:50%;border:2px solid var(--blue);display:flex;align-items:center;justify-content:center}
.contact-item .ring span{width:50px;height:50px;border-radius:50%;background:var(--blue);display:flex;align-items:center;justify-content:center}
.contact-item small{display:block;color:var(--gold);font-size:14px;margin-bottom:4px}
.contact-item strong{color:var(--blue);font-size:19px;font-weight:700}
.divider{position:absolute;top:40px;width:1px;height:44px;background:#e3e3e3}
.nav-bar{position:absolute;left:0;top:122px;width:1200px;height:78px}
.main-nav{position:absolute;left:378px;top:150px;display:flex;gap:30px;font-size:15px;color:var(--white)}
.main-nav .active{color:var(--gold-light)}
.nav-pin{position:absolute;left:393px;top:114px;width:17px;height:17px;border-radius:50%;background:var(--gold)}
.social{position:absolute;display:flex;gap:12px}
.social span{width:40px;height:40px;border-radius:50%;display:block}
.head-social{left:922px;top:140px}
.head-social span{border:2px solid var(--white)}

/* hero */
.hero-photo{position:absolute;left:0;top:200px;width:805px;height:735px;background:linear-gradient(120deg,#f2f1ee 0%,#e4e2dd 45%,#8f9297 70%,#54575c 100%)}
.hero-right-photo{position:absolute;left:805px;top:640px;width:395px;height:295px;background:linear-gradient(160deg,#dbeef8,#7a8c6a 60%,#5d4c3b)}
.welcome{position:absolute;left:113px;top:282px;font-size:36px;color:var(--ink);letter-spacing:1px}
.hero-name{position:absolute;left:108px;top:335px;font-size:86px;line-height:.95;font-weight:800;color:var(--gold)}
.btn-outline{position:absolute;left:113px;top:527px;width:148px;height:51px;border:2px solid var(--gold);color:var(--gold);font-weight:700;font-size:15px;display:flex;align-items:center;justify-content:center}
.slider-dots{position:absolute;left:560px;top:856px;display:flex;gap:6px;align-items:center}
.slider-dots span{width:12px;height:12px;border-radius:50%;background:var(--white)}
.slider-dots .on{width:14px;height:14px;background:var(--gold);border:2px solid var(--white)}
.contact-panel{position:absolute;left:805px;top:200px;width:395px;height:440px;background:var(--pale)}
.contact-panel h2{position:absolute;left:0;width:395px;top:36px;text-align:center;font-size:30px;font-weight:500;color:var(--ink)}
.field{position:absolute;left:23px;width:334px;height:52px;background:var(--white);border:1px solid #dfe7ee;font-size:14px;color:var(--muted);padding:16px 22px}
.btn-gold{position:absolute;background:linear-gradient(90deg,var(--gold-light),var(--gold));color:var(--ink);font-weight:700;display:flex;align-items:center;justify-content:center}
.submit{left:23px;top:378px;width:140px;height:50px;font-size:16px}

/* headings */
.section-title{position:absolute;left:0;width:1200px;text-align:center;font-size:31px;font-weight:700;color:var(--ink);display:flex;align-items:center;justify-content:center;gap:12px}
.mark{display:inline-block;width:28px;height:34px;flex:none}

/* about */
.about-art{position:absolute;left:110px;top:1050px;width:440px;height:440px;background:radial-gradient(circle,#9fb6c7 0%,#c7d6a8 40%,#ffffff 72%)}
.about-title{position:absolute;left:598px;top:1097px;font-size:31px;font-weight:700;color:var(--ink);display:flex;align-items:center;gap:12px}
.about-text{position:absolute;left:598px;top:1168px;width:496px;font-size:14.5px;line-height:26px;color:var(--text)}
.learn-more{left:598px;top:1385px;width:157px;height:52px;font-size:15px}

/* services */
.services{position:absolute;left:0;top:1578px;width:1200px;height:642px;background:linear-gradient(135deg,#f3f9fd,#e2f1fa)}
.service-card{position:absolute;top:1752px;width:315px;height:384px;background:var(--white);box-shadow:0 4px 14px rgba(0,0,0,.05)}
.service-card svg{position:absolute;left:0;top:0}
.service-card h3{position:absolute;left:0;width:315px;top:198px;text-align:center;font-size:27px;font-weight:500;color:var(--ink)}
.service-card p{position:absolute;left:20px;width:275px;top:248px;text-align:center;font-size:14.5px;line-height:26px}
.service-card a{position:absolute;left:0;width:315px;top:342px;text-align:center;font-size:15px;font-weight:700;color:var(--blue)}

/* how it works */
.step{position:absolute;top:2397px;width:174px;height:174px;border-radius:50%;border:3px solid var(--gold);display:flex;align-items:center;justify-content:center}
.step.alt{border-color:var(--blue)}
.step .core{width:152px;height:152px;border-radius:50%;background:var(--blue);display:flex;align-items:center;justify-content:center}
.step.alt .core{background:var(--gold)}
.step-label{position:absolute;top:2594px;width:260px;text-align:center;font-size:22px;font-weight:600;color:var(--ink)}

/* testimonials */
.testimonials{position:absolute;left:0;top:2705px;width:1200px;height:538px;background:linear-gradient(180deg,#2aa4e2,#1a96d6)}
.testimonials .section-title{color:var(--white)}
.quote-card{position:absolute;top:2885px;width:470px;height:275px;background:var(--white)}
.quote-card .chev{position:absolute;left:0;top:50px}
.avatar{position:absolute;left:68px;top:40px;width:106px;height:106px;border-radius:50%;background:linear-gradient(160deg,#c9ced5,#3a3f47);border:4px solid var(--white);box-shadow:0 0 0 1px #e5e5e5}
.quote-card h4{position:absolute;left:178px;top:63px;font-size:22px;font-weight:600;color:var(--gold)}
.quote-card .role{position:absolute;left:178px;top:97px;font-size:14.5px;color:var(--ink)}
.quote-card p{position:absolute;left:173px;top:140px;width:280px;font-size:14.5px;line-height:26px}
.quote-card .qm{position:absolute;left:40px;top:165px;font-size:130px;line-height:1;color:#f6ecd3;font-family:Georgia,serif}
.arrow-btn{position:absolute;top:2996px;width:52px;height:52px;border-radius:50%;display:flex;align-items:center;justify-content:center}

/* blogs */
.blog-feature-photo{position:absolute;left:124px;top:3423px;width:463px;height:318px;background:linear-gradient(135deg,#6a4a32,#c79b74 50%,#3e2c20)}
.blog-feature{position:absolute;left:158px;top:3604px;width:464px;height:196px;background:var(--white);border:1px solid #e5e5e5}
.date{display:flex;align-items:center;gap:8px;font-size:13px;color:var(--muted)}
.date i{width:13px;height:13px;border:2px solid var(--blue);border-radius:50%;display:block}
.blog-feature .date{position:absolute;left:26px;top:28px}
.blog-feature h5{position:absolute;left:26px;top:60px;font-size:15px;font-weight:600;color:var(--ink)}
.blog-feature p{position:absolute;left:26px;top:96px;width:360px;font-size:11px;line-height:18px;color:var(--muted)}
.read{font-size:14px;font-weight:700;color:var(--gold);letter-spacing:.5px}
.blog-feature .read{position:absolute;left:26px;top:155px}
.pager{position:absolute;left:407px;width:32px;height:32px;display:flex;align-items:center;justify-content:center}
.blog-thumb{position:absolute;left:645px;width:190px;height:176px}
.blog-item{position:absolute;left:862px;width:230px}
.blog-item h5{font-size:15px;font-weight:600;color:var(--ink);line-height:25px;margin:14px 0 12px}
.blog-item p{font-size:11px;line-height:19px;color:var(--text);margin-bottom:14px}

/* footer */
.site-footer{position:absolute;left:0;top:3885px;width:1200px;height:361px;background:var(--footer);color:var(--white)}
.footer-brand{left:110px;top:95px;font-size:24px;width:170px;line-height:1.1}
.footer-line{position:absolute;left:388px;top:55px;width:1px;height:215px;background:#2b2c2f}
.foot-col{position:absolute;top:56px}
.foot-col h6{font-size:20px;font-weight:600;margin-bottom:16px}
.foot-col li{list-style:none;font-size:14px;line-height:26px}
.foot-col li::before{content:"»";margin-right:12px}
.foot-col li.active{color:var(--gold)}
.foot-contact{font-size:14px;line-height:24px;display:flex;gap:10px;margin-bottom:16px}
.copyright{position:absolute;left:110px;top:318px;font-size:14px}
.foot-social{left:918px;top:308px;gap:8px}
.foot-social span{width:37px;height:37px;background:var(--blue);border:2px solid var(--white)}
</style>
</head>
<body>

<header class="site-header">
  <div class="brand header-brand"><span class="dot"></span>Brightvale Crew</div>

  <div class="contact-item" style="left:375px">
    <div class="ring"><span>
      <svg width="24" height="24" viewBox="0 0 24 24"><path d="M6 3l3 4-2 2c1 3 4 6 7 7l2-2 4 3-2 4C10 21 3 14 3 5z" fill="none" stroke="#fff" stroke-width="1.6"/></svg>
    </span></div>
    <div><small>Call Now :</small><strong>+1 (555) 014 2288</strong></div>
  </div>
  <div class="divider" style="left:655px"></div>
  <div class="contact-item" style="left:682px">
    <div class="ring"><span>
      <svg width="24" height="24" viewBox="0 0 24 24"><rect x="3" y="6" width="18" height="13" rx="2" fill="none" stroke="#fff" stroke-width="1.6"/><path d="M3 7l9 7 9-7" fill="none" stroke="#fff" stroke-width="1.6"/></svg>
    </span></div>
    <div><small>Email :</small><strong>info@brightvalecrew.example</strong></div>
  </div>
  <div class="divider" style="left:1022px"></div>
  <svg class="abs" style="left:1048px;top:50px" width="22" height="22" viewBox="0 0 22 22"><circle cx="9" cy="9" r="6" fill="none" stroke="#e2b43c" stroke-width="2"/><path d="M13 13l6 6" stroke="#e2b43c" stroke-width="2"/></svg>

  <svg class="nav-bar" width="1200" height="78" viewBox="0 0 1200 78">
    <polygon points="360,0 905,0 878,78 315,78" fill="#1a9fdf"/>
    <polygon points="905,0 1140,0 1185,78 878,78" fill="#e2b43c"/>
  </svg>
  <span class="nav-pin"></span>
  <nav class="main-nav">
    <a class="active">Home</a><a>About</a><a>Services</a><a>How its work</a><a>Blog</a><a>Contact</a>
  </nav>
  <div class="social head-social"><span></span><span></span><span></span></div>
</header>

<section class="hero">
  <div class="hero-photo" role="img" aria-label="Photo of a smiling man working on a laptop on a grey sofa in a bright living room"></div>
  <div class="hero-right-photo" role="img" aria-label="Photo of a potted plant beside the sofa"></div>
  <div class="welcome">WELCOME TO</div>
  <div class="hero-name">BRIGHTVALE<br>CREW</div>
  <a class="btn-outline">GET STARTED</a>
  <div class="slider-dots"><span></span><span></span><span class="on"></span><span></span></div>

  <form class="contact-panel">
    <h2>Contact</h2>
    <div class="field" style="top:93px">Name</div>
    <div class="field" style="top:156px">Phone</div>
    <div class="field" style="top:218px">Email</div>
    <div class="field" style="top:280px;height:85px">Address</div>
    <div class="btn-gold submit">SUBMIT</div>
  </form>
</section>

<section class="about">
  <div class="about-art" role="img" aria-label="Illustrated star figure collage with photos of homes, a family and office scenes"></div>
  <h2 class="about-title">
    <svg class="mark" viewBox="0 0 28 34"><circle cx="6" cy="20" r="5" fill="#e2b43c"/><path d="M10 2l14 15-14 15 6-15z" fill="#1a9fdf"/></svg>
    ABOUT BRIGHTVALE CREW
  </h2>
  <p class="about-text">Lorem ipsum dolor sit amet, consectetur adipiscing elit, se eiusmod tempor incididunt ut labore et dolore magna aliqua. Ut enim a minim veniam, quis nostrud exercitation ullamco laboris nisi ut aliquip ex ea commodo consequat. Duis aute irure dolor in reprehenderi voluptate velit esse cillum dolore eu fugiat nulla pariatur. Excepteur s occaecat cupidatat non proident, sunt in culpa qui officia deserunt mollit ani id est laborum.</p>
  <a class="btn-gold learn-more">LEARN MORE</a>
</section>

<section class="services">
  <h2 class="section-title" style="top:88px">
    <svg class="mark" viewBox="0 0 28 34"><circle cx="6" cy="20" r="5" fill="#e2b43c"/><path d="M10 2l14 15-14 15 6-15z" fill="#1a9fdf"/></svg>
    OUR SERVICES
  </h2>
</section>

<article class="service-card" style="left:110px">
  <svg width="315" height="190" viewBox="0 0 315 190" role="img" aria-label="Photo of a team meeting around a table"><polygon points="0,0 315,0 315,24 157,180 0,24" fill="#8f8c86"/><polyline points="0,24 157,180 315,24" fill="none" stroke="#1a9fdf" stroke-width="5"/></svg>
  <h3>Lorem ipsum</h3>
  <p>Sed ut perspiciatis unde omnis iste natus error accusantiumdoloremque laudantiumtotam rem aperiam</p>
  <a>Learn More</a>
</article>
<article class="service-card" style="left:442px">
  <svg width="315" height="190" viewBox="0 0 315 190" role="img" aria-label="Photo of colleagues smiling at a laptop"><polygon points="0,0 315,0 315,24 157,180 0,24" fill="#a7b2bc"/><polyline points="0,24 157,180 315,24" fill="none" stroke="#1a9fdf" stroke-width="5"/></svg>
  <h3>Lorem ipsum</h3>
  <p>Sed ut perspiciatis unde omnis iste natus error accusantiumdoloremque laudantiumtotam rem aperiam</p>
  <a>Learn More</a>
</article>
<article class="service-card" style="left:772px">
  <svg width="315" height="190" viewBox="0 0 315 190" role="img" aria-label="Photo of coworkers reviewing notes at a desk"><polygon points="0,0 315,0 315,24 157,180 0,24" fill="#9c9791"/><polyline points="0,24 157,180 315,24" fill="none" stroke="#1a9fdf" stroke-width="5"/></svg>
  <h3>Lorem ipsum</h3>
  <p>Sed ut perspiciatis unde omnis iste natus error accusantiumdoloremque laudantiumtotam rem aperiam</p>
  <a>Learn More</a>
</article>

<section class="how-it-works">
  <h2 class="section-title" style="top:2303px">
    <svg class="mark" viewBox="0 0 28 34"><circle cx="6" cy="20" r="5" fill="#e2b43c"/><path d="M10 2l14 15-14 15 6-15z" fill="#1a9fdf"/></svg>
    HOW IT WORKS
  </h2>
  <div class="step" style="left:171px"><div class="core">
    <svg width="80" height="80" viewBox="0 0 80 80" fill="none" stroke="#fff" stroke-width="2.5"><path d="M10 38L38 14l28 24"/><path d="M18 32v34h28"/><rect x="28" y="42" width="12" height="24"/><circle cx="56" cy="58" r="12"/><path d="M56 51v14M52 55h7"/></svg>
  </div></div>
  <div class="step alt" style="left:512px"><div class="core">
    <svg width="80" height="80" viewBox="0 0 80 80" fill="none" stroke="#fff" stroke-width="2.5"><rect x="10" y="14" width="54" height="40"/><path d="M20 46V36M30 46V30M40 46V38"/><circle cx="52" cy="38" r="10"/><path d="M59 45l10 10"/><path d="M24 54l-6 14M50 54l6 14"/></svg>
  </div></div>
  <div class="step" style="left:853px"><div class="core">
    <svg width="80" height="80" viewBox="0 0 80 80" fill="none" stroke="#fff" stroke-width="2.5"><circle cx="40" cy="26" r="10"/><circle cx="40" cy="26" r="16" stroke-dasharray="5 4"/><path d="M8 50l16-8 14 6 12-6 22 8-22 16H24z"/></svg>
  </div></div>
  <svg class="abs" style="left:370px;top:2460px" width="120" height="40" viewBox="0 0 120 40"><path d="M4 20C30 0 80 0 110 24" fill="none" stroke="#555" stroke-width="1.5" stroke-dasharray="5 4"/><path d="M102 22l9 3-4-9" fill="none" stroke="#555" stroke-width="1.5"/></svg>
  <svg class="abs" style="left:712px;top:2472px" width="120" height="40" viewBox="0 0 120 40"><path d="M4 14C34 34 84 34 112 10" fill="none" stroke="#555" stroke-width="1.5" stroke-dasharray="5 4"/><path d="M104 9l9 0-3 9" fill="none" stroke="#555" stroke-width="1.5"/></svg>
  <div class="step-label" style="left:128px">Lorem ipsum</div>
  <div class="step-label" style="left:469px">Lorem ipsum</div>
  <div class="step-label" style="left:810px">Lorem ipsum</div>
</section>

<section class="testimonials" role="img" aria-label="Blue tinted photo background of people smiling">
  <h2 class="section-title" style="top:88px">
    <svg class="mark" viewBox="0 0 28 34"><circle cx="6" cy="20" r="5" fill="#fff"/><path d="M10 2l14 15-14 15 6-15z" fill="#fff"/></svg>
    ORU TESTIMONIALS
  </h2>
</section>
<div class="arrow-btn" style="left:37px;background:var(--gold)"><svg width="24" height="14" viewBox="0 0 24 14"><path d="M22 7H3M9 1L3 7l6 6" fill="none" stroke="#fff" stroke-width="2"/></svg></div>
<div class="arrow-btn" style="left:1111px;background:var(--white)"><svg width="24" height="14" viewBox="0 0 24 14"><path d="M2 7h19M15 1l6 6-6 6" fill="none" stroke="#e2b43c" stroke-width="2"/></svg></div>

<article class="quote-card" style="left:110px">
  <svg class="chev" width="100" height="120" viewBox="0 0 100 120"><path d="M0 60L60 0C30 30 30 90 60 120z" fill="#1a9fdf"/></svg>
  <div class="avatar" role="img" aria-label="Portrait photo of a client in a suit"></div>
  <h4>DANIEL</h4>
  <div class="role">Nemo enim ipsam</div>
  <p>Lorem ipsum dolor sit am consectetur adipiscing elit, sed do eiusmo tempor incididunt ut labore &nbsp;aliqua.perspiciatis unde omnis iste natus error sit</p>
  <div class="qm">&ldquo;</div>
</article>
<article class="quote-card" style="left:617px">
  <svg class="chev" width="100" height="120" viewBox="0 0 100 120"><path d="M0 60L60 0C30 30 30 90 60 120z" fill="#1a9fdf"/></svg>
  <div class="avatar" role="img" aria-label="Portrait photo of a client in a suit"></div>
  <h4>DANIEL</h4>
  <div class="role">Nemo enim ipsam</div>
  <p>Lorem ipsum dolor sit am consectetur adipiscing elit, sed do eiusmo tempor incididunt ut labore &nbsp;aliqua.perspiciatis unde omnis iste natus error sit</p>
  <div class="qm">&ldquo;</div>
</article>

<section class="blogs">
  <h2 class="section-title" style="top:3320px">
    <svg class="mark" viewBox="0 0 28 34"><circle cx="6" cy="20" r="5" fill="#e2b43c"/><path d="M10 2l14 15-14 15 6-15z" fill="#1a9fdf"/></svg>
    LATEST FROM BLOGS
  </h2>
  <div class="blog-feature-photo" role="img" aria-label="Photo of two friends laughing together"></div>
  <article class="blog-feature">
    <div class="date"><i></i>April 21.2022</div>
    <h5>Sed ut perspiciatis unde omnis iste</h5>
    <p>Lorem ipsum dolor sit amet, consectetur adipiscing elit, sed do eiusmod tempor incididunt ut labore et dolore magna</p>
    <a class="read">READ MORE &nbsp;→</a>
    <div class="pager" style="top:28px;background:var(--blue)"><svg width="10" height="14" viewBox="0 0 10 14"><path d="M2 1l6 6-6 6" fill="none" stroke="#fff" stroke-width="2"/></svg></div>
    <div class="pager" style="top:70px;background:#cfcfcf"><svg width="10" height="14" viewBox="0 0 10 14"><path d="M8 1L2 7l6 6" fill="none" stroke="#fff" stroke-width="2"/></svg></div>
  </article>

  <div class="blog-thumb" style="top:3420px;background:linear-gradient(180deg,#8fb3d6,#c9c7c2 55%,#4f7a3a)" role="img" aria-label="Photo of a suburban house with a lawn"></div>
  <article class="blog-item" style="top:3414px">
    <div class="date"><i></i>April 21.2022</div>
    <h5>Sed ut perspiciatis unde omnis iste</h5>
    <p>Lorem ipsum dolor sit a consectetur adipiscing elit, sed do eiusm tempor incididunt</p>
    <a class="read">READ MORE &nbsp;→</a>
  </article>

  <div class="blog-thumb" style="top:3624px;background:linear-gradient(180deg,#d59a98,#9a8a7e 55%,#4e7a34)" role="img" aria-label="Photo of a large house at dusk"></div>
  <article class="blog-item" style="top:3618px">
    <div class="date"><i></i>April 21.2022</div>
    <h5>Sed ut perspiciatis unde omnis iste</h5>
    <p>Lorem ipsum dolor sit a consectetur adipiscing elit, sed do eiusm tempor incididunt</p>
    <a class="read">READ MORE &nbsp;→</a>
  </article>
</section>

<footer class="site-footer">
  <div class="brand footer-brand"><span class="dot"></span>Brightvale Crew</div>
  <div class="footer-line"></div>
  <div class="foot-col" style="left:432px">
    <h6>Quick Links</h6>
    <ul><li class="active">Home</li><li>About</li><li>Services</li><li>How its work</li><li>Blog</li><li>Contact</li></ul>
  </div>
  <div class="foot-col" style="left:640px">
    <h6>Our Company</h6>
    <ul><li>Terms&amp;condtions</li><li>Privacy Policy</li><li>About Us</li><li>Support</li></ul>
  </div>
  <div class="foot-col" style="left:864px">
    <h6>Contact us</h6>
    <div class="foot-contact"><svg width="12" height="18" viewBox="0 0 12 18"><path d="M6 17C2 11 1 9 1 6a5 5 0 0110 0c0 3-1 5-5 11z" fill="#fff"/><circle cx="6" cy="6" r="2" fill="#111"/></svg><span>Lorem ipsum dolor sit<br>amet, consectetur adipiscing</span></div>
    <div class="foot-contact"><svg width="14" height="14" viewBox="0 0 24 24"><path d="M6 3l3 4-2 2c1 3 4 6 7 7l2-2 4 3-2 4C10 21 3 14 3 5z" fill="#fff"/></svg><span>1+ (555) 014 2288</span></div>
    <div class="foot-contact"><svg width="16" height="14" viewBox="0 0 16 12"><rect width="16" height="12" rx="1" fill="#fff"/><path d="M1 1l7 6 7-6" fill="none" stroke="#111" stroke-width="1.2"/></svg><span>info@brightvalecrew.example</span></div>
  </div>
  <div class="copyright">©Copyrights 2022 Brightvale Crew &nbsp;| &nbsp;&nbsp;All Rights Reserved</div>
  <div class="social foot-social"><span></span><span></span><span></span><span></span></div>
</footer>

</body>
</html>
```